Business card for home developer

Name, email, phone #, logo, address, lic # and slogan.
Slogan to say something like, "Leader in quality neighborhood communities" maybe? The last one said "Building higher, living better". Some thing saying we are above the other people.
Updates
The card can be two sided?
Target Market(s)
Home buyers
Industry/Entity Type
Business
Look and feel
Each slider illustrates characteristics of the customer's brand and the style your logo design should communicate.

```html
<!DOCTYPE html>
<html lang="en">
<head>
<meta charset="utf-8">
<title>Summit Crest Homes — Business Card</title>
<link rel="stylesheet" href="https://fonts.googleapis.com/css2?family=Roboto:wght@400;900&family=Dancing+Script:wght@500&family=Kalam:wght@700&display=swap">
<style>
  :root {
    --backdrop: #2a2a2a;
    --cream: #fff6b8;
    --cream-edge: #f7d94a;
    --wood-light: #c98a45;
    --wood-mid: #a8652a;
    --wood-dark: #7a3f12;
    --navy: #2b3f86;
    --slogan: #3b4a8c;
    --white: #ffffff;
  }
  * { box-sizing: border-box; margin: 0; padding: 0; }
  html, body {
    width: 1200px; height: 935px; overflow: hidden;
    background: var(--backdrop);
  }
  .sheet {
    position: relative; width: 1200px; height: 935px;
    display: flex; align-items: center; justify-content: center; gap: 26px;
  }
  .card {
    position: relative; width: 563px; height: 346px; overflow: hidden;
  }
  .wood {
    position: absolute; inset: 0;
    background: radial-gradient(ellipse at 50% 55%, var(--wood-light) 0%, var(--wood-mid) 55%, var(--wood-dark) 100%);
  }
  .band {
    position: absolute; left: 0; right: 0;
    background: var(--cream);
    border: 4px solid var(--cream-edge);
    display: flex; align-items: center; justify-content: center;
  }
  .card--front .band { top: 0; height: 128px; }
  .card--back .band { top: 114px; height: 122px; }
  .brand {
    display: flex; flex-direction: column; align-items: center;
  }
  .brand__row { display: flex; align-items: center; gap: 8px; }
  .brand__name {
    font-family: "Roboto", Arial, sans-serif; font-weight: 900;
    font-size: 30px; letter-spacing: 0.5px; color: var(--navy);
    text-transform: uppercase;
  }
  .brand__dot {
    width: 18px; height: 18px; border-radius: 50%; background: var(--navy);
  }
  .brand__slogan {
    font-family: "Dancing Script", cursive; font-weight: 500;
    font-size: 24px; color: var(--slogan);
    margin-top: 2px;
  }
  .card--front .brand { margin-left: 90px; }
  .holder {
    position: absolute; left: 34px; top: 222px;
    font-family: "Roboto", Arial, sans-serif; font-size: 24px; color: var(--white);
  }
  .contact {
    position: absolute; left: 330px; top: 150px; list-style: none;
    font-family: "Kalam", cursive; font-weight: 700; font-size: 22px;
    line-height: 34px; color: var(--white);
  }
</style>
</head>
<body>
<main class="sheet">
  <section class="card card--front">
    <div class="wood" role="img" aria-label="Warm wood grain texture"></div>
    <header class="band">
      <div class="brand">
        <div class="brand__row">
          <span class="brand__dot"></span>
          <span class="brand__name">Summit Crest Homes</span>
        </div>
        <p class="brand__slogan">Building higher, living better</p>
      </div>
    </header>
    <p class="holder">Your Name</p>
    <ul class="contact">
      <li>Address</li>
      <li>Phone #</li>
      <li>E-mail</li>
      <li>Lic #</li>
    </ul>
  </section>

  <section class="card card--back">
    <div class="wood" role="img" aria-label="Warm wood grain texture"></div>
    <div class="band">
      <div class="brand">
        <div class="brand__row">
          <span class="brand__dot"></span>
          <span class="brand__name">Summit Crest Homes</span>
        </div>
        <p class="brand__slogan">Building higher, living better</p>
      </div>
    </div>
  </section>
</main>
</body>
</html>
```